Looking for someone to design a business card for my plumbing business Brindle Plumbing Solutions I want the background also to be black, must attract clients. If possible I want the front to be the logo and the back to show maybe the details.

Target Market(s)

Clients

Industry/Entity Type

Plumbing maintenance

Contact Information for Business Card

Name: Dylan, Contact: 0451 306 729, Email: brindleplumbingsolutions@mailpost.example, Licence number 728094K

Font styles to use
Other font styles liked:
• as per logo maybe?

Colors

Designer to choose colors to be used in the design.

Requirements
Nice to have
• stating the service I provide, emergency plumbing, plumbing maintenance, drainage maintenance, block sewer and stormwater, camera and locating.

```html
<!DOCTYPE html>
<html lang="en">
<head>
<meta charset="UTF-8">
<title>Brindle Plumbing Solutions – Business Card</title>
<link href="https://fonts.googleapis.com/css2?family=Montserrat:wght@400;700;800&display=swap" rel="stylesheet">
<style>
  :root {
    --stage: #3a3a3c;
    --card: #121213;
    --ink: #ffffff;
    --accent: #4a8fd6;
    --muted: #d9d9d9;
  }
  * { margin: 0; padding: 0; box-sizing: border-box; }
  html, body { width: 1200px; height: 689px; overflow: hidden; }
  body {
    background: var(--stage);
    font-family: "Montserrat", sans-serif;
    display: flex;
    align-items: center;
    justify-content: center;
    gap: 48px;
  }
  .card {
    position: relative;
    width: 540px;
    height: 309px;
    background: var(--card);
    border-radius: 22px;
    box-shadow: 0 18px 40px rgba(0,0,0,0.45);
    overflow: hidden;
  }
  .card-front {
    display: flex;
    align-items: center;
    justify-content: center;
  }
  .brand-name {
    font-weight: 800;
    text-transform: uppercase;
    letter-spacing: 0.02em;
    line-height: 1.05;
    text-align: center;
  }
  .card-front .brand-name {
    color: var(--ink);
    font-size: 34px;
  }
  .card-back .brand-name {
    position: absolute;
    left: 70px;
    top: 58px;
    color: var(--accent);
    font-size: 26px;
    text-align: left;
  }
  .holder-name {
    position: absolute;
    left: 70px;
    top: 168px;
    color: var(--accent);
    font-weight: 700;
    font-size: 30px;
  }
  .contact-list {
    position: absolute;
    left: 70px;
    top: 220px;
    list-style: none;
    color: var(--ink);
    font-size: 14px;
    font-weight: 400;
  }
  .contact-list li {
    display: flex;
    align-items: center;
    gap: 10px;
    margin-bottom: 8px;
  }
  .contact-icon { width: 14px; height: 14px; flex: none; }
  .licence {
    position: absolute;
    right: 36px;
    top: 34px;
    color: var(--muted);
    font-size: 13px;
  }
</style>
</head>
<body>
  <section class="card card-front" aria-label="Card front">
    <p class="brand-name">Brindle<br>Plumbing Solutions</p>
  </section>

  <section class="card card-back" aria-label="Card back">
    <p class="brand-name">Brindle<br>Plumbing Solutions</p>
    <p class="licence">Licence number 728094K</p>
    <p class="holder-name">Dylan</p>
    <ul class="contact-list">
      <li>
        <svg class="contact-icon" viewBox="0 0 24 24" aria-hidden="true">
          <path fill="#4a8fd6" d="M6.6 10.8a15.1 15.1 0 0 0 6.6 6.6l2.2-2.2a1 1 0 0 1 1-.25 11.4 11.4 0 0 0 3.6.57 1 1 0 0 1 1 1V20a1 1 0 0 1-1 1A17 17 0 0 1 3 4a1 1 0 0 1 1-1h3.5a1 1 0 0 1 1 1c0 1.25.2 2.45.57 3.57a1 1 0 0 1-.25 1z"/>
        </svg>
        <span>0451 306 729</span>
      </li>
      <li>
        <svg class="contact-icon" viewBox="0 0 24 24" aria-hidden="true">
          <rect x="2" y="5" width="20" height="14" rx="1.5" fill="#4a8fd6"/>
          <path d="M3 6.5l9 6.5 9-6.5" fill="none" stroke="#121213" stroke-width="1.8"/>
        </svg>
        <span>brindleplumbingsolutions@mailpost.example</span>
      </li>
    </ul>
  </section>
</body>
</html>
```